Research and Innovation programme/projects in WOOD based industries

1.Tesarka s.r.o. (offical registered brand name of our company)
-Managing technology development projects
-International cooperation and development European projects
Our company was founded in 2008 and started to work as a counsilary company operating in the section of european funds administrated by Czech republic. Nowadays we are specializing on projects in the sphere of science and research co-financed by EU.Since 6.6.2013 we are registered under European comission for a purpose of broad support of transnational projects.

Target Market(s)

We are primarily focused on european companies, which stand behind the latest research and innovation of sawing, planing, glulam and logging technologies based on wooden materials.

Coding

Coded - Design and coding required

Number of Pages Required

5+ page

Font styles to use
Serif

Colors
cadf82
abd037
9bcb3c
fee18a
ffcf3e
ffc214

Requirements
Must have
• The web will exist in three possible languages in czech, english and deutsch.
• First page : introduction of a company
• Second page : Area of expertise
• Third page: servicies our company provides
• Fourth page: Our partners
• Fifth page: Conditions of our servicies
• Sixth page: Succesful projects
• - we would also love if we had possibility to add videos about our successful projects
• Seventh: Our team
• We are serious company in the sphere of funds and counsilary servicies, that is why we would love to have web design as representative as possible
• Take on mind that that we are specializing on development management, try to apply that on your design
• In the section of contacts, we would love to have photos of our team,
• This is our current site: http://www.tesarka-example.eu/cz/partneri.html
• This is how our concurency sites are lookin. Take these designs as an slight inspiration.
• http://www.quilmatek-example.sk/en/
• https://www2.brantwell-example.com/global/en.html
Nice to have
• Visible logo on the front page for the visitor.
• As a inspiration we provided link for our current web design, but we dont want to copy the current style, just look at the logo and the pages that exists on current web.
• !!!!!!We also uploaded file, where we explain how our cooperation with partner works. Especially in the part 2. section of service. Take that as an ispiration too, or use that to understand, what our company do.
Should not have
• We are serious company in the sphere of funds and counsilary servicies, that is why we would love to have web design representative as possible

```html
<!DOCTYPE html>
<html lang="de">
<head>
<meta charset="utf-8">
<title>1. Tesarka s.r.o. – Das Unternehmen</title>
<link href="https://fonts.googleapis.com/css2?family=Montserrat:wght@700&family=Poiret+One&family=Poppins:wght@300;400;500;600;700&display=swap" rel="stylesheet">
<style>
  :root {
    --green-dark: #0b8a3e;
    --green-brand: #1f8f3a;
    --green-button: #7dc22a;
    --orange: #ffa400;
    --orange-head: #f9a11b;
    --header-bg: #2b2b2b;
    --band-gold: #f9cb53;
    --band-pale: #f9df7c;
    --ink: #1d1d1d;
    --text: #3a3a3a;
    --white: #ffffff;
    --shadow-box: #d5dee5;
    --icon-grey: #9a9a9a;
    --footer-bg: #050505;
  }
  * { box-sizing: border-box; margin: 0; padding: 0; }
  html, body { width: 918px; height: 1200px; overflow: hidden; background: var(--white); }
  body { font-family: "Poppins", sans-serif; color: var(--text); }
  .page { position: relative; width: 918px; height: 1200px; overflow: hidden; }
  .abs { position: absolute; }

  .topbar { left: 0; top: 0; width: 918px; height: 17px; background: var(--green-dark); color: var(--white); font-size: 7.4px; line-height: 17px; }
  .topbar .contact { position: absolute; left: 156px; }
  .topbar .langs { position: absolute; right: 156px; }
  .topbar .sep { margin: 0 5px; }

  .header { left: 0; top: 17px; width: 918px; height: 95px; background: var(--header-bg); }
  .brand-square { left: 156px; top: 16px; width: 61px; height: 61px; background: var(--white); }
  .brand-name { left: 256px; top: 24px; font-size: 16.5px; font-weight: 700; color: var(--green-brand); }
  .brand-tag { left: 257px; top: 48px; font-size: 11px; font-weight: 700; color: var(--orange); }
  .page-title { right: 160px; top: 30px; font-family: "Poiret One", sans-serif; font-size: 17px; color: var(--white); }

  .nav { left: 0; top: 112px; width: 918px; height: 25px; background: var(--orange); border-top: 1px solid #d98a00; }
  .nav ul { list-style: none; position: absolute; left: 191px; top: 0; display: flex; gap: 23px; }
  .nav li { font-size: 7.8px; font-weight: 600; color: var(--white); line-height: 24px; }

  .hero { left: 0; top: 137px; width: 918px; height: 191px;
    background: radial-gradient(ellipse at 35% 60%, #4f7a1f 0%, #6a9a24 35%, #93c92e 70%, #b6e12c 100%); }
  .hero-title { left: 191px; top: 64px; font-size: 28.5px; font-weight: 700; color: var(--white); }
  .hero-sub { left: 191px; top: 104px; font-size: 22.5px; font-weight: 300; color: var(--white); }

  .enterprise-title { left: 187px; top: 370px; font-family: "Montserrat", sans-serif; font-size: 18px; font-weight: 700; color: var(--orange-head); }
  .enterprise-text { left: 189px; top: 405px; width: 290px; font-size: 7.3px; line-height: 11.5px; }
  .enterprise-text p { margin-bottom: 11.5px; }
  .btn { left: 189px; top: 537px; width: 75px; height: 19px; background: var(--green-button); color: var(--white); font-size: 8px; text-align: center; line-height: 19px; }
  .photo-back { left: 545px; top: 371px; width: 206px; height: 184px; background: var(--shadow-box); }
  .photo { left: 530px; top: 356px; width: 207px; height: 184px;
    background: radial-gradient(circle at 40% 45%, #b9a58a 0%, #7d6a55 55%, #4b3f33 100%); }

  .philosophy-title { left: 0; width: 918px; top: 615px; text-align: center; font-family: "Montserrat", sans-serif; font-size: 18px; font-weight: 700; color: var(--ink); }

  .band { left: 0; width: 918px; }
  .band-gold { background: var(--band-gold); }
  .band-pale { background: var(--band-pale); }
  .topic h3 { font-size: 12px; font-weight: 600; color: var(--ink); }
  .topic .rule { width: 28px; height: 2px; background: var(--ink); margin: 6px 0 14px; }
  .topic p { width: 312px; font-size: 7.3px; line-height: 11.5px; color: var(--ink); }
  .art { background: linear-gradient(90deg, #2b7c98 0%, #2b7c98 40%, #a3161a 60%, #a3161a 100%); }

  .footer { left: 0; top: 1151px; width: 918px; height: 49px; background: var(--footer-bg); }
  .footer-text { left: 159px; top: 19px; font-size: 7.5px; color: var(--white); }
  .social { position: absolute; top: 13px; }
</style>
</head>
<body>
<div class="page">

  <div class="abs topbar">
    <span class="contact">1. Tesarka s.r.o, ID 4816<span class="sep">|</span>Lindenweg 14<span class="sep">|</span>01234 Musterstadt</span>
    <span class="langs">English<span class="sep">|</span>Czech<span class="sep">|</span>Deutsch</span>
  </div>

  <header class="abs header">
    <div class="abs brand-square"></div>
    <div class="abs brand-name">1. Tesarka s.r.o</div>
    <div class="abs brand-tag">Beratungsfirma</div>
    <div class="abs page-title">Das Unternehmen</div>
  </header>

  <nav class="abs nav">
    <ul>
      <li>Das Unternehmen</li>
      <li>Leistungen</li>
      <li>Unsere Projekte</li>
      <li>Kooperationspartner</li>
      <li>Anrufe für die Zusammenarbeit</li>
      <li>Kontakt</li>
    </ul>
  </nav>

  <section class="abs hero" role="img" aria-label="Green abstract background">
    <h1 class="abs hero-title">Dont Find Solution!</h1>
    <p class="abs hero-sub">We are here to help you.</p>
  </section>

  <h2 class="abs enterprise-title">THE ENTERPRISE</h2>
  <div class="abs enterprise-text">
    <p>We start with the administration of EU projects and state aid projects. At present we are working for completed portfolio of clients as supervisors of development and innovative projects.</p>
    <p>The company 1.Tesarka is registered since 04.04.2008 in the commercial register under ID: 30451276.</p>
    <p>Since the 06.06.2013 our company is under the registration number 482093715563-27 as "1. Tesarka s.r.o. "has been registered in the Register of European Commission Representatives.</p>
  </div>
  <div class="abs btn">Read More</div>
  <div class="abs photo-back"></div>
  <div class="abs photo" role="img" aria-label="Photo of stacked cut logs"></div>

  <h2 class="abs philosophy-title">OUR PHILOSOPHY</h2>

  <section class="abs band band-gold" style="top:660px;height:160px;">
    <div class="abs topic" style="left:159px;top:31px;">
      <h3>Chef</h3><div class="rule"></div>
      <p>Nullam maximus bibendum leo non accumsan. Sed vehicula odio ut lacinia mollis. Morbi nulla justo, scelerisque id ligula nec, feugiat varius enim. Fusce malesuada, felis at placerat mattis, leo massa pulvinar nulla, vel efficitur quam dolor quis lacus. Vestibulum ante ipsum primis in faucibus orci luctus et ultrices posuere cubilia Curae; Aenean auctor,</p>
    </div>
    <div class="abs art" style="left:502px;top:20px;width:249px;height:124px;" role="img" aria-label="Illustration of a leader standing out from a row of people"></div>
  </section>

  <section class="abs band band-pale" style="top:820px;height:165px;">
    <div class="abs art" style="left:156px;top:21px;width:250px;height:124px;" role="img" aria-label="Illustration of a straight path beside a tangled path"></div>
    <div class="abs topic" style="left:443px;top:32px;">
      <h3>Meinung</h3><div class="rule"></div>
      <p>Nullam maximus bibendum leo non accumsan. Sed vehicula odio ut lacinia mollis. Morbi nulla justo, scelerisque id ligula nec, feugiat varius enim. Fusce malesuada, felis at placerat mattis, leo massa pulvinar nulla, vel efficitur quam dolor quis lacus. Vestibulum ante ipsum primis in faucibus orci luctus et ultrices posuere cubilia Curae; Aenean auctor,</p>
    </div>
  </section>

  <section class="abs band band-gold" style="top:985px;height:166px;">
    <div class="abs topic" style="left:159px;top:32px;">
      <h3>Umgang mit Problemen</h3><div class="rule"></div>
      <p>Nullam maximus bibendum leo non accumsan. Sed vehicula odio ut lacinia mollis. Morbi nulla justo, scelerisque id ligula nec, feugiat varius enim. Fusce malesuada, felis at placerat mattis, leo massa pulvinar nulla, vel efficitur quam dolor quis lacus. Vestibulum ante ipsum primis in faucibus orci luctus et ultrices posuere cubilia Curae; Aenean auctor,</p>
    </div>
    <div class="abs art" style="left:504px;top:22px;width:249px;height:123px;" role="img" aria-label="Illustration of footsteps walking around an obstacle"></div>
  </section>

  <footer class="abs footer">
    <div class="abs footer-text">© 2019, All Righst Reserved, Lindenweg 14,&nbsp; 01234 Musterstadt</div>
    <svg class="social" style="left:647px;" width="114" height="20" viewBox="0 0 114 20" aria-label="Social links">
      <circle cx="10" cy="10" r="9.5" fill="var(--icon-grey)"/>
      <circle cx="33" cy="10" r="9.5" fill="var(--icon-grey)"/>
      <circle cx="56.5" cy="10" r="9.5" fill="var(--icon-grey)"/>
      <circle cx="80" cy="10" r="9.5" fill="var(--icon-grey)"/>
      <circle cx="103" cy="10" r="9.5" fill="var(--icon-grey)"/>
    </svg>
  </footer>

</div>
</body>
</html>
```